Pinecrest Haulers ~ A+ Division of Vantor

Energetic ,different ,exotic ,modern,
never before done, next level buisness card for a trash dumpster company
is for a trash removal construction company ...please have your wildest ideas i dont want a boring basic buisness card i want people to say wow !! And be able to mention you and who designed my card ...i know you take pride in your work i do to ....3 years ago quillwork from brief hive made a logo for me and i still love it .....use his colors and the word vantor DO NOT USE ROOFING AND REMODELING use Pinecrest Haulers ....look at his Logo i Like the [S] LOGO and word Vantor ....you surprise me and we will do alot more projects with you and or brief hive ....thank you for your hard work and your time i do appreciate all of you and admire your skills designing .....i really do appreciate all of you thank you -todd
Ps Lets make these biz cards special different from many ,unique

Target Market(s)

Construction .....dumpsters trash Trash removal

Industry/Entity Type

Construction

Contact Information for Business Card

Black gold white maybe more colors

Requirements
Must have
• Vantor ~Pinecrest Haulers division Serving Atlanta and surrounding areas'Chief executive Todd Marlow cell 404 555 0147 Office 404 888 8888Follow us on fb ,instagram .. email Pinecresthaulers-demo.com Hablamos espaƱol
Nice to have
• Black gold white colors like my logo i updated and you can add more if you want ....its a construction / trucking company dumpster Trash company we recycle also
Should not have
• When you look at my logo (Must not have roofing and remodeling )

```html
<!DOCTYPE html>
<html lang="en">
<head>
<meta charset="utf-8">
<title>Vantor – Pinecrest Haulers Business Card</title>
<link rel="stylesheet" href="https://fonts.googleapis.com/css2?family=Exo+2:wght@400;600;700;900&family=Tinos:wght@700&display=swap">
<style>
  :root {
    --backdrop: #1b1b1b;
    --card-light: #ececec;
    --card-light-top: #f2f2f2;
    --gold: #f0b81a;
    --gold-deep: #ddaa22;
    --gold-bright: #f8d21a;
    --ink: #1a1a1a;
    --text: #222222;
    --social: #3a5a98;
  }
  * { margin: 0; padding: 0; box-sizing: border-box; }
  html, body { width: 1200px; height: 900px; overflow: hidden; }
  body {
    background: var(--backdrop);
    position: relative;
    font-family: "Exo 2", sans-serif;
    color: var(--text);
  }
  .card {
    position: absolute;
    top: 170px;
    width: 347px;
    height: 561px;
    box-shadow: 3px 4px 8px rgba(0,0,0,.6);
    overflow: hidden;
  }
  .card--front {
    left: 259px;
    background: linear-gradient(var(--card-light-top), var(--card-light));
  }
  .card--back {
    left: 631px;
    background: radial-gradient(circle at 55% 45%, var(--gold-bright), var(--gold-deep) 75%);
  }

  .brand {
    position: absolute;
    top: 86px;
    left: 29px;
    display: flex;
    align-items: center;
    gap: 9px;
  }
  .brand__mark {
    width: 62px; height: 62px;
    background: linear-gradient(135deg, var(--gold-bright), var(--gold-deep));
  }
  .brand__text { display: flex; flex-direction: column; }
  .brand__name {
    font-weight: 900;
    font-size: 40px;
    line-height: 36px;
    letter-spacing: 9px;
    color: var(--ink);
  }
  .brand__division {
    font-weight: 700;
    font-size: 9px;
    line-height: 12px;
    letter-spacing: 5.6px;
    color: var(--gold);
    white-space: nowrap;
  }
  .service-area {
    position: absolute;
    top: 172px; left: 0; width: 100%;
    text-align: center;
    font-size: 14px;
    letter-spacing: .3px;
  }
  .language {
    position: absolute;
    top: 196px; left: 0; width: 100%;
    text-align: center;
    font-size: 12px;
    font-weight: 600;
    color: var(--gold);
  }
  .person {
    position: absolute;
    top: 252px; left: 0; width: 100%;
    text-align: center;
  }
  .person__name {
    font-weight: 700;
    font-size: 23px;
    color: var(--gold);
    line-height: 1.1;
  }
  .person__role { font-size: 15px; line-height: 1.2; }

  .divider {
    display: flex;
    align-items: center;
    justify-content: center;
    gap: 4px;
  }
  .divider::before, .divider::after {
    content: ""; width: 48px; height: 1px; background: #555;
  }
  .divider--icons { position: absolute; top: 307px; left: 0; width: 100%; }
  .icon {
    width: 12px; height: 12px;
    background: var(--gold);
    border-radius: 2px;
    display: flex; align-items: center; justify-content: center;
  }
  .contacts {
    position: absolute;
    top: 322px; left: 0; width: 100%;
    text-align: center;
    font-size: 15px;
    line-height: 20px;
  }
  .divider--follow {
    position: absolute; top: 419px; left: 0; width: 100%;
    font-size: 12.5px; font-weight: 600; color: var(--gold);
  }
  .divider--follow::before, .divider--follow::after { width: 38px; }
  .social {
    position: absolute; top: 442px; left: 0; width: 100%;
    display: flex; justify-content: center; gap: 4px;
  }
  .social__square { width: 20px; height: 20px; background: var(--social); }
  .motto {
    position: absolute;
    bottom: 0; left: 0; width: 100%; height: 73px;
    background: linear-gradient(var(--gold-bright), var(--gold));
    font-family: "Tinos", serif;
    font-weight: 700;
    font-size: 19px;
    line-height: 22px;
    text-align: center;
    padding-top: 14px;
    color: var(--ink);
  }

  .back-emblem {
    position: absolute;
    top: 55px; left: 20px;
    width: 304px; height: 420px;
    background: linear-gradient(160deg, rgba(255,230,60,.35), rgba(200,150,20,.25));
  }
  .back-name {
    position: absolute;
    top: 476px; left: 0; width: 100%;
    text-align: center;
    font-weight: 900;
    font-size: 50px;
    line-height: 44px;
    letter-spacing: 12px;
    padding-left: 12px;
    color: var(--ink);
  }
  .back-division {
    position: absolute;
    top: 516px; left: 0; width: 100%;
    text-align: center;
    font-weight: 700;
    font-size: 11px;
    letter-spacing: 7px;
    padding-left: 7px;
    color: var(--ink);
    white-space: nowrap;
  }
</style>
</head>
<body>
  <section class="card card--front">
    <div class="brand">
      <div class="brand__mark"></div>
      <div class="brand__text">
        <div class="brand__name">VANTOR</div>
        <div class="brand__division">PINECREST HAULERS</div>
      </div>
    </div>
    <p class="service-area">SERVING ATLANTA AND SURROUNDING AREAS</p>
    <p class="language">Hablamos español</p>

    <div class="person">
      <p class="person__name">TODD MARLOW</p>
      <p class="person__role">Chief executive</p>
    </div>

    <div class="divider divider--icons">
      <span class="icon"><svg width="6" height="8" viewBox="0 0 6 8"><rect x=".5" y=".5" width="5" height="7" rx="1" fill="none" stroke="#fff"/></svg></span>
      <span class="icon"><svg width="8" height="6" viewBox="0 0 8 6"><path d="M1 4 Q4 0 7 4 V5 H1Z" fill="#fff"/></svg></span>
      <span class="icon"><svg width="8" height="6" viewBox="0 0 8 6"><rect x=".5" y=".5" width="7" height="5" fill="none" stroke="#fff"/><path d="M.5 .5 4 3.5 7.5 .5" fill="none" stroke="#fff"/></svg></span>
      <span class="icon"><svg width="8" height="8" viewBox="0 0 8 8"><circle cx="4" cy="4" r="3.2" fill="none" stroke="#fff"/><path d="M1 4h6M4 1v6" stroke="#fff" stroke-width=".8"/></svg></span>
    </div>

    <div class="contacts">
      <p>404 555 0147</p>
      <p>404 555 0162</p>
      <p>info@pinecresthaulers-demo.com</p>
      <p>www.pinecresthaulers-demo.com</p>
    </div>

    <div class="divider divider--follow">FOLLOW US ON</div>
    <div class="social">
      <span class="social__square"></span>
      <span class="social__square"></span>
    </div>

    <div class="motto">LIFE BEGINS AT THE END<br>OF YOUR COMFORT ZONE</div>
  </section>

  <section class="card card--back">
    <div class="back-emblem" role="img" aria-label="Large faint brand emblem area"></div>
    <div class="back-name">VANTOR</div>
    <div class="back-division">PINECREST HAULERS</div>
  </section>
</body>
</html>
```